Marriage Podcast Needs Cover Art

The name of the marriage podcast is "Lantern Hearth", representing a bond between the husband, wife, and God. The artwork needs to include a rope tied in a heart shape and the podcast name (Lantern Hearth). I prefer a simple background, but a subtle pattern would be okay too. In general, simplicity is better. The artwork should be easy on the eyes. This cover art is what my listeners will see in their podcast app next to each episode name. The image is small, so the text needs to be large enough to read in this context. This means there will not be enough room for large pockets of blank space. The design basically fills the entire canvas.

Please see the attachment for some suggestions. Thanks! :)

Target Market(s)

Young married couples

Industry/Entity Type

Rope

Requirements
Must have
• - Rope tied in a heart shape.
• - Text: "Lantern Hearth"
• - 1400 x 1400 pixels
Nice to have
• - Bright or warm colors that convey love/marriage
• - 3000 x 3000 pixels
Should not have
• Dark or muted-color background

```html
<!DOCTYPE html>
<html lang="en">
<head>
<meta charset="utf-8">
<title>Lantern Hearth Podcast</title>
<link rel="stylesheet" href="https://fonts.googleapis.com/css2?family=League+Spartan:wght@700;900&display=swap">
<style>
  :root {
    --red-centre: #f20c0c;
    --red-edge: #b50000;
    --rope-light: #86369a;
    --rope-dark: #6a2266;
    --gold: #f6c81f;
    --gold-deep: #eeb11c;
    --shadow-purple: #7d3a97;
  }
  html, body {
    margin: 0;
    padding: 0;
    width: 1200px;
    height: 1200px;
    overflow: hidden;
  }
  .cover {
    width: 1200px;
    height: 1200px;
    background: radial-gradient(circle at 50% 48%, var(--red-centre) 0%, #e80808 45%, var(--red-edge) 100%);
    position: relative;
  }
  .cover svg {
    position: absolute;
    inset: 0;
    display: block;
  }
  .title-word {
    font-family: "League Spartan", "Futura", sans-serif;
    font-weight: 900;
  }
  .title-shadow { fill: var(--shadow-purple); }
  .title-face { fill: url(#goldFace); }
  .subtitle {
    font-family: "League Spartan", "Futura", sans-serif;
    font-weight: 700;
    fill: var(--gold);
  }
  .title-rule { fill: var(--gold); }
  .title-rule-shadow { fill: var(--shadow-purple); }
</style>
</head>
<body>
<main class="cover">
  <svg viewBox="0 0 1200 1200" width="1200" height="1200" xmlns="http://www.w3.org/2000/svg">
    <defs>
      <radialGradient id="ropeTone" cx="0.5" cy="0.55" r="0.6">
        <stop offset="0.55" stop-color="var(--rope-light)"/>
        <stop offset="1" stop-color="var(--rope-dark)"/>
      </radialGradient>
      <linearGradient id="goldFace" x1="0" y1="0" x2="1" y2="0">
        <stop offset="0" stop-color="var(--gold-deep)"/>
        <stop offset="0.5" stop-color="var(--gold)"/>
        <stop offset="1" stop-color="var(--gold-deep)"/>
      </linearGradient>
    </defs>

    <path class="rope-heart" role="img" aria-label="Braided purple rope tied in a heart shape, knotted at the top and bottom"
          d="M600 262 C 540 172, 380 150, 280 178 C 160 212, 112 320, 122 440 C 140 620, 340 790, 600 962 C 860 790, 1060 620, 1078 440 C 1088 320, 1040 212, 920 178 C 820 150, 660 172, 600 262 Z"
          fill="none" stroke="url(#ropeTone)" stroke-width="92" stroke-linejoin="round"/>

    <g class="title">
      <text class="title-word title-shadow" x="271" y="529" font-size="238" textLength="620" lengthAdjust="spacingAndGlyphs">LANTERN</text>
      <text class="title-word title-face" x="285" y="519" font-size="238" textLength="620" lengthAdjust="spacingAndGlyphs">LANTERN</text>

      <rect class="title-rule-shadow" x="314" y="548" width="541" height="18"/>
      <rect class="title-rule" x="326" y="539" width="541" height="18"/>

      <text class="title-word title-shadow" x="337" y="720" font-size="186" textLength="510" lengthAdjust="spacingAndGlyphs">HEARTH</text>
      <text class="title-word title-face" x="351" y="710" font-size="186" textLength="510" lengthAdjust="spacingAndGlyphs">HEARTH</text>

      <text class="subtitle" x="474" y="776" font-size="55" textLength="257" lengthAdjust="spacingAndGlyphs">PODCAST</text>
    </g>
  </svg>
</main>
</body>
</html>
```